Florida-based Coastal Landscaping Comapny Needs Postcard Designs

We are a newly established Florida-based, coastal landscaping company that is looking for some really innovative postcards that we can use to get our name our to affluent consumers that live on the coast of Florida (think on the beach) and small to medium sized businesses in the same area. We will be sending out 100s of thousands of these, so need a great design

Target Market(s)

Affluent consumers and small to medium sized businesses

Industry/Entity Type

Landscaping

Font styles to use
Sans Serif

Colors

Designer to choose colors to be used in the design.

Requirements
Must have
• Florida - looking, island looking / paradise, but incorporate landscaping themes
• Need to say something about "Enjoy your yard this summer" or something relating to summer, landscapes and florida
• and would like to make two offers $50.00 off with signing up for one of our routine maintenance programs, or 1 free landscape inspection
Should not have
• Regular generic lawn company designs. We are a top tier landscape design / build plus maintenance firm, so not your mom and pop lawn mowing company

```html
<!DOCTYPE html>
<html lang="en">
<head>
<meta charset="utf-8">
<title>Shorecrest Summer Postcard</title>
<link rel="stylesheet" href="https://fonts.googleapis.com/css2?family=Lobster&family=Roboto+Condensed:wght@400;700&family=Open+Sans:wght@400;600&display=swap">
<style>
  :root{
    --brand-blue:#13a4d8;
    --ink:#2b2b2b;
    --charcoal:#333538;
    --stage:#636363;
    --paper:#ffffff;
  }
  html,body{margin:0;padding:0;overflow:hidden;}
  body{width:1200px;height:1200px;background:var(--paper);position:relative;}
  .stage{position:absolute;left:0;top:133px;width:1200px;height:636px;background:var(--stage);}
  .postcard{position:absolute;top:229px;width:541px;height:420px;box-shadow:0 8px 10px rgba(0,0,0,.45);}
  .postcard--front{left:35px;}
  .postcard--back{left:619px;}
  .postcard svg{display:block;width:100%;height:100%;}
  .logo{font-family:"Open Sans",sans-serif;font-weight:600;fill:var(--ink);letter-spacing:1px;}
  .headline{font-family:"Lobster",sans-serif;}
  .cond{font-family:"Roboto Condensed",sans-serif;}
  .body{font-family:"Open Sans",sans-serif;}
</style>
</head>
<body>
<div class="stage"></div>

<!-- Front side -->
<div class="postcard postcard--front">
<svg viewBox="0 0 631 490" xmlns="http://www.w3.org/2000/svg">
  <defs>
    <linearGradient id="frontPaper" x1="0" y1="0" x2="1" y2="0">
      <stop offset="0" stop-color="#ffffff"/><stop offset="1" stop-color="#d9d9d9"/>
    </linearGradient>
    <linearGradient id="islandTones" x1="0" y1="0" x2="0" y2="1">
      <stop offset="0" stop-color="#3aa7b0"/><stop offset=".4" stop-color="#2f7d3c"/><stop offset=".75" stop-color="#3f8f4a"/><stop offset="1" stop-color="#1aa596"/>
    </linearGradient>
    <radialGradient id="badgeFill" cx=".4" cy=".35" r=".7">
      <stop offset="0" stop-color="#ffffff"/><stop offset="1" stop-color="#d4d4d4"/>
    </radialGradient>
  </defs>
  <rect width="631" height="490" fill="url(#frontPaper)"/>

  <path role="img" aria-label="Aerial photograph of a tropical island with villas, palms and turquoise water"
        d="M0 70 C80 130 200 178 340 186 C470 196 570 166 631 147 L631 340 C520 345 470 352 420 362 C300 370 150 385 0 395 Z" fill="url(#islandTones)"/>

  <!-- top swooshes -->
  <path d="M40 0 L95 0 C175 95 245 165 340 175 C470 186 570 156 631 137 L631 147 C570 166 470 196 340 186 C220 176 110 100 40 0 Z" fill="var(--charcoal)"/>
  <path d="M95 0 L130 0 C190 95 250 158 340 168 C470 178 570 148 631 130 L631 137 C570 156 470 186 340 175 C245 165 175 95 95 0 Z" fill="var(--brand-blue)"/>

  <!-- bottom bands -->
  <path d="M420 352 C500 350 560 420 631 470 L631 490 L600 490 C560 430 500 372 420 358 Z" fill="var(--paper)"/>
  <path d="M430 360 C500 370 540 440 565 490 L535 490 C510 440 480 390 430 366 Z" fill="var(--brand-blue)"/>
  <path d="M500 400 C560 430 600 460 631 465 L631 490 L585 490 C560 450 530 420 500 410 Z" fill="var(--charcoal)"/>

  <text class="logo" x="403" y="51" text-anchor="middle" font-size="21" textLength="194" lengthAdjust="spacingAndGlyphs">SHORECREST</text>
  <text class="headline" x="401" y="111" text-anchor="middle" font-size="40" fill="var(--brand-blue)" textLength="284" lengthAdjust="spacingAndGlyphs">Enjoy Your Yard</text>
  <text class="headline" x="400" y="152" text-anchor="middle" font-size="31" fill="var(--ink)" textLength="177" lengthAdjust="spacingAndGlyphs">This Summer</text>

  <text class="cond" x="46" y="427" font-size="29" fill="var(--ink)" textLength="343" lengthAdjust="spacingAndGlyphs"><tspan font-weight="700" fill="var(--brand-blue)">$50.00 OFF</tspan> WITH SIGNING UP</text>
  <text class="cond" x="46" y="452" font-size="20" fill="var(--ink)" textLength="341" lengthAdjust="spacingAndGlyphs">for one of our routine maintenance programs</text>

  <circle cx="492" cy="390" r="70" fill="var(--charcoal)"/>
  <circle cx="492" cy="390" r="64" fill="url(#badgeFill)"/>
  <text class="cond" x="489" y="403" text-anchor="middle" font-size="40" font-weight="700" fill="var(--brand-blue)" textLength="116" lengthAdjust="spacingAndGlyphs">1 FREE</text>
  <text class="cond" x="489" y="419" text-anchor="middle" font-size="14" fill="var(--ink)" textLength="112" lengthAdjust="spacingAndGlyphs">Landscape Inspection</text>
</svg>
</div>

<!-- Back side -->
<div class="postcard postcard--back">
<svg viewBox="0 0 631 490" xmlns="http://www.w3.org/2000/svg">
  <defs>
    <linearGradient id="homeTones" x1="0" y1="0" x2="0" y2="1">
      <stop offset="0" stop-color="#5aa6e0"/><stop offset=".45" stop-color="#d8c3a3"/><stop offset=".75" stop-color="#5d8a3c"/><stop offset="1" stop-color="#8aa36a"/>
    </linearGradient>
    <radialGradient id="badgeFillBack" cx=".4" cy=".35" r=".7">
      <stop offset="0" stop-color="#ffffff"/><stop offset="1" stop-color="#d4d4d4"/>
    </radialGradient>
  </defs>
  <rect width="631" height="490" fill="var(--paper)"/>

  <path role="img" aria-label="Photograph of a Florida home with palm trees and a landscaped front yard"
        d="M0 0 L335 0 C310 50 298 110 292 160 C200 180 90 195 0 210 Z" fill="url(#homeTones)"/>
  <path d="M0 205 C90 190 190 170 250 160 L245 176 C170 188 80 205 0 225 Z" fill="var(--brand-blue)"/>

  <!-- divider swooshes -->
  <path d="M335 0 L358 0 C315 60 300 120 300 200 C300 300 330 380 318 490 L308 490 C318 380 292 300 292 200 C292 120 305 60 335 0 Z" fill="var(--brand-blue)"/>
  <path d="M296 255 C312 330 316 410 298 490 L288 490 C302 410 300 330 290 262 Z" fill="var(--charcoal)"/>

  <text class="logo" x="405" y="93" text-anchor="middle" font-size="17" textLength="135" lengthAdjust="spacingAndGlyphs">SHORECREST</text>
  <rect x="507" y="45" width="84" height="84" fill="none" stroke="var(--ink)" stroke-width="1"/>
  <g stroke="var(--ink)" stroke-width="1">
    <line x1="364" y1="300" x2="587" y2="300"/>
    <line x1="364" y1="334" x2="587" y2="334"/>
    <line x1="364" y1="368" x2="587" y2="368"/>
  </g>

  <circle cx="278" cy="191" r="70" fill="var(--charcoal)"/>
  <circle cx="278" cy="191" r="64" fill="url(#badgeFillBack)"/>
  <text class="cond" x="275" y="203" text-anchor="middle" font-size="40" font-weight="700" fill="var(--brand-blue)" textLength="117" lengthAdjust="spacingAndGlyphs">1 FREE</text>
  <text class="cond" x="275" y="219" text-anchor="middle" font-size="14" fill="var(--ink)" textLength="113" lengthAdjust="spacingAndGlyphs">Landscape Inspection</text>

  <text class="body" x="22" y="243" font-size="12" font-weight="600" fill="var(--ink)" textLength="186" lengthAdjust="spacingAndGlyphs"><tspan fill="var(--brand-blue)">Lorem Ipsum is</tspan> simply dummy</text>
  <g class="body" font-size="11" fill="var(--ink)">
    <circle cx="25" cy="259" r="2" fill="var(--brand-blue)"/><text x="32" y="263" textLength="184" lengthAdjust="spacingAndGlyphs">text of the printing and typesetting</text>
    <circle cx="25" cy="274" r="2" fill="var(--brand-blue)"/><text x="32" y="278" textLength="187" lengthAdjust="spacingAndGlyphs">industry. Lorem Ipsum has been the</text>
    <circle cx="25" cy="289" r="2" fill="var(--brand-blue)"/><text x="32" y="293" textLength="192" lengthAdjust="spacingAndGlyphs">industry's standard dummy text ever</text>
  </g>

  <rect x="15" y="311" width="277" height="62" rx="12" fill="none" stroke="var(--brand-blue)" stroke-width="2"/>
  <text class="cond" x="29" y="342" font-size="22" fill="var(--ink)" textLength="250" lengthAdjust="spacingAndGlyphs"><tspan font-weight="700" fill="var(--brand-blue)">$50.00 OFF</tspan> WITH SIGNING UP</text>
  <text class="cond" x="29" y="359" font-size="15" fill="var(--ink)" textLength="247" lengthAdjust="spacingAndGlyphs">for one of our routine maintenance programs</text>

  <path d="M0 398 C120 385 230 395 285 440 L282 490 L0 490 Z" fill="var(--brand-blue)"/>
  <path d="M0 406 C120 395 225 405 277 445 L275 490 L0 490 Z" fill="var(--charcoal)"/>
  <g class="body" font-size="12.5" font-weight="600" fill="var(--paper)">
    <circle cx="23" cy="438" r="5" fill="none" stroke="var(--brand-blue)" stroke-width="1.5"/>
    <text x="33" y="442" textLength="84" lengthAdjust="spacingAndGlyphs">xxx.xxxxx.xxx</text>
    <rect x="128" y="434" width="10" height="7" fill="none" stroke="var(--brand-blue)" stroke-width="1.5"/>
    <text x="142" y="442" textLength="106" lengthAdjust="spacingAndGlyphs">companymail@id</text>
    <circle cx="23" cy="461" r="5" fill="var(--brand-blue)"/>
    <text x="33" y="465" textLength="126" lengthAdjust="spacingAndGlyphs">www.cowebsite.com</text>
  </g>
</svg>
</div>
</body>
</html>
```